Dining hall menu app needs a redesign

We are looking for a redesign of our app PlateView which is available for iOS for free on the Orchard Appmarket.

The app allows students of most of Germany's universities to show the menu of their university's dining hall. Currently there are about 400 dining halls to view the menu of. A menu contains the a list of meals for the next couple of days (usually for the next 5-7 days). Each meal can be rated by the users and photos can be uploaded. The following data should be visible for each meal in the meal list:
- The date the meal is available
- The meal category (usually a short text, categorizing the meal)
- Name of the meal (can be very long but it's ok to truncate it after the second line)
- Average meal rating (5-star rating)
- A photo of the meal
- Up to 4 prices (e.g. usually students pay less than employees, which is why multiple prices for the same meal are available. In the menu list only the prices are shown)

When selecting a meal, more details about the meal are shown:
- Full meal name
- Up to 4 prices including the price type (e.g. Student: 3.40€, Employees: 4.20€)
- Total number of ratings
- Total number of comments
- A list of additives and info-texts about the meal (e.g. whether the meal is vegetarian, or contains food additives)
- A list of photos including a relative date when the photo has been taken (e.g. "2 months ago")

Additionally a user should be able to add a review to the meal (5 star rating and an optional comment), view the list of comments, take a photo of the meal and to share it on friendlink/chirpa/via email.

All views show an advertisement banner on the bottom of the view.

The design should be very modern and clean. We don't like a skeuomorphic design. The content of the app is most important. Other than that you are free to design something pretty.
Updates

Target Market(s)

Students (age between 19 and 30)

Industry/Entity Type

University

Requirements
Must have
• At least we need a redesign of the meal list, the meal detail page, the app-logo and the splashscreen.
Nice to have
• Design for the meal review page, the dining hall list and the favorites list.
Should not have
• No skeuomorphic design and not too many colors.

```html
<!DOCTYPE html>
<html lang="en">
<head>
<meta charset="utf-8">
<title>PlateView – Meal list</title>
<link rel="stylesheet" href="https://fonts.googleapis.com/css2?family=Comfortaa:wght@600;700&family=Varela+Round&display=swap">
<style>
:root{
  --page-bg:#ece7df;
  --status-bg:#0d0d0d;
  --green:#4cc784;
  --green-dark:#34a96a;
  --green-light:#7fe0a6;
  --mint:#c8ecd8;
  --list-bg:#dde8e0;
  --card-bg:#f8f7ec;
  --ink:#4b4b4b;
  --ink-soft:#6f6f6f;
  --date-ink:#7b8a80;
  --star-off:#dcdcdc;
  --price:#ee6668;
  --price-dark:#d94e52;
  --ad-red:#c8241a;
  --white:#ffffff;
}
*{box-sizing:border-box;margin:0;padding:0}
html,body{width:1200px;height:870px;overflow:hidden;background:var(--page-bg)}
body{position:relative;font-family:"Varela Round",sans-serif;color:var(--ink)}

.screen{position:absolute;left:325px;top:23px;width:550px;height:824px;overflow:hidden;background:var(--list-bg);box-shadow:0 4px 18px rgba(0,0,0,.18)}

.status-bar{position:absolute;left:0;top:0;width:100%;height:32px;background:var(--status-bg);color:var(--white);font-size:18px;line-height:32px}
.status-bar .carrier{position:absolute;left:10px;top:0;display:flex;align-items:center;gap:6px;height:32px}
.status-bar .time{position:absolute;left:0;right:0;top:0;text-align:center}
.status-bar svg{display:block}
.status-bar .battery{position:absolute;right:10px;top:8px}

.app-bar{position:absolute;top:32px;left:0;width:100%;height:77px;background:linear-gradient(var(--green-light),var(--green) 55%,var(--green-dark))}
.app-title{position:absolute;left:0;right:0;top:17px;text-align:center;font-family:"Comfortaa",sans-serif;font-weight:700;font-size:38px;line-height:44px;color:var(--white);letter-spacing:.5px}
.back-button{position:absolute;left:13px;top:14px;width:84px;height:46px;background:var(--green-dark);border-radius:6px;clip-path:polygon(14px 0,100% 0,100% 100%,14px 100%,0 50%);color:var(--white);font-family:"Comfortaa",sans-serif;font-weight:700;font-size:20px;display:flex;align-items:center;justify-content:center;padding-left:10px}
.refresh-button{position:absolute;right:10px;top:14px;width:54px;height:46px;background:var(--green-dark);border-radius:7px;display:flex;align-items:center;justify-content:center}

.date-bar{position:absolute;top:109px;left:0;width:100%;height:48px;background:var(--mint);border-bottom:3px dotted var(--white);display:flex;align-items:center;justify-content:center;gap:72px;color:var(--date-ink);font-size:18px}

.meal-card{position:absolute;left:5px;width:540px;height:152px;background:var(--card-bg);border-radius:4px;box-shadow:0 1px 2px rgba(0,0,0,.12);overflow:hidden}
.meal-photo{position:absolute;left:0;top:0;width:152px;height:152px}
.photo-rice{background:radial-gradient(circle at 50% 50%,#e8e6dd 0%,#c9c7bd 45%,#8f8a84 75%,#b9b1a8 100%)}
.photo-fries{background:radial-gradient(circle at 50% 45%,#f1d98a 0%,#e4c266 40%,#cfa27a 70%,#eae6e0 100%)}
.photo-add{background:var(--green);display:flex;align-items:center;justify-content:center}
.meal-info{position:absolute;left:164px;top:6px}
.meal-name{font-family:"Comfortaa",sans-serif;font-weight:700;font-size:27px;line-height:32px;color:var(--ink)}
.meal-desc{font-size:18px;line-height:22px;color:var(--ink-soft);margin-top:1px}
.rating{display:flex;gap:4px;margin-top:6px}
.rating svg{width:28px;height:28px}
.star-on{fill:var(--green)}
.star-off{fill:var(--star-off)}
.price-tag{display:inline-flex;align-items:center;height:38px;margin-top:7px;border-radius:5px;background:var(--price);color:var(--white);font-size:24px;overflow:hidden;box-shadow:0 2px 0 var(--price-dark)}
.price-tag .basket{width:42px;height:100%;display:flex;align-items:center;justify-content:center;border-right:1px solid rgba(255,255,255,.35)}
.price-tag .amounts{padding:0 12px 0 10px;white-space:nowrap}
.price-tag .sep{font-size:19px;opacity:.7;margin:0 5px}
.price-tag .cur{font-size:17px;margin-right:1px}

.ad-banner{position:absolute;left:0;top:736px;width:100%;height:88px;background:linear-gradient(90deg,#7fb2d9,#a9cfe6 45%,#9ec0a4)}
.ad-badge{position:absolute;left:6px;top:6px;width:42px;height:42px;background:#2a76c6;border-radius:4px}
.ad-artwork{position:absolute;left:54px;top:0;width:360px;height:88px;background:linear-gradient(90deg,#b4806a,#8fb7d6 50%,#c9c4b0)}
.ad-button{position:absolute;right:10px;top:16px;height:56px;padding:0 16px;background:linear-gradient(#e23a2c,var(--ad-red));border:3px solid #f3efe6;border-radius:6px;color:var(--white);font-family:"Comfortaa",sans-serif;font-weight:700;font-size:28px;display:flex;align-items:center}
.ad-info{position:absolute;left:6px;bottom:5px;width:16px;height:16px;border:1px solid var(--white);border-radius:50%;color:var(--white);font-size:11px;text-align:center;line-height:14px}
</style>
</head>
<body>
<svg width="0" height="0" style="position:absolute">
  <defs>
    <symbol id="star" viewBox="0 0 24 24"><polygon points="12,1.5 15,8.6 22.6,9.2 16.8,14.2 18.6,21.8 12,17.8 5.4,21.8 7.2,14.2 1.4,9.2 9,8.6"/></symbol>
    <symbol id="basket" viewBox="0 0 24 24"><path d="M3 9h18l-2 10H5z M8 9l3-5 M16 9l-3-5" fill="none" stroke="#fff" stroke-width="2" stroke-linejoin="round"/><path d="M9 12v5M12 12v5M15 12v5" stroke="#fff" stroke-width="1.6"/></symbol>
    <symbol id="add-photo" viewBox="0 0 80 80"><rect x="30" y="8" width="44" height="32" rx="7" fill="#fff"/><rect x="44" y="3" width="16" height="8" rx="2" fill="#fff"/><circle cx="52" cy="24" r="9" fill="#4cc784"/><circle cx="52" cy="24" r="5" fill="#fff"/><rect x="6" y="48" width="28" height="8" rx="2" fill="#fff"/><rect x="16" y="38" width="8" height="28" rx="2" fill="#fff"/></symbol>
  </defs>
</svg>

<main class="screen">
  <div class="status-bar">
    <div class="carrier">
      <svg width="30" height="16" viewBox="0 0 30 16"><rect x="0" y="11" width="4" height="5" fill="#fff"/><rect x="6" y="8" width="4" height="8" fill="#fff"/><rect x="12" y="5" width="4" height="11" fill="#fff"/><rect x="18" y="2" width="4" height="14" fill="#fff"/><rect x="24" y="0" width="4" height="16" fill="#fff"/></svg>
      <span>NetWave</span>
      <svg width="26" height="18" viewBox="0 0 26 18"><path d="M1 6a17 17 0 0 1 24 0M5 10a11 11 0 0 1 16 0M9 14a5 5 0 0 1 8 0" fill="none" stroke="#fff" stroke-width="2.4"/></svg>
    </div>
    <div class="time">12:34 PM</div>
    <svg class="battery" width="36" height="17" viewBox="0 0 36 17"><rect x="1" y="1" width="31" height="15" rx="2" fill="none" stroke="#fff" stroke-width="1.5"/><rect x="3.5" y="3.5" width="26" height="10" fill="#fff"/><rect x="33" y="5" width="2.5" height="7" fill="#fff"/></svg>
  </div>

  <header class="app-bar">
    <div class="back-button">Back</div>
    <h1 class="app-title">PlateView</h1>
    <div class="refresh-button">
      <svg width="28" height="28" viewBox="0 0 24 24"><path d="M19 12a7 7 0 1 1-2.1-5" fill="none" stroke="#fff" stroke-width="2.6" stroke-linecap="round"/><polygon points="14,3 21,3 21,10" fill="#fff"/></svg>
    </div>
  </header>

  <nav class="date-bar"><span>&lt;</span><span>Today May 15, 2013</span><span>&gt;</span></nav>

  <article class="meal-card" style="top:165px">
    <div class="meal-photo photo-rice" role="img" aria-label="Photo of a bowl of butter rice with herbs"></div>
    <div class="meal-info">
      <h2 class="meal-name">Butterreis</h2>
      <p class="meal-desc">this contains additives</p>
      <div class="rating"><svg class="star-on"><use href="#star"/></svg><svg class="star-on"><use href="#star"/></svg><svg class="star-on"><use href="#star"/></svg><svg class="star-on"><use href="#star"/></svg><svg class="star-off"><use href="#star"/></svg></div>
      <div class="price-tag"><span class="basket"><svg width="20" height="20"><use href="#basket"/></svg></span><span class="amounts"><span class="cur">€</span>12<span class="sep">/</span><span class="cur">€</span>14.50</span></div>
    </div>
  </article>

  <article class="meal-card" style="top:322px">
    <div class="meal-photo photo-add"><svg width="80" height="80"><use href="#add-photo"/></svg></div>
    <div class="meal-info">
      <h2 class="meal-name">Maccaronelli</h2>
      <p class="meal-desc">maccaronelli</p>
      <div class="rating"><svg class="star-on"><use href="#star"/></svg><svg class="star-on"><use href="#star"/></svg><svg class="star-off"><use href="#star"/></svg><svg class="star-off"><use href="#star"/></svg><svg class="star-off"><use href="#star"/></svg></div>
      <div class="price-tag"><span class="basket"><svg width="20" height="20"><use href="#basket"/></svg></span><span class="amounts"><span class="cur">€</span>1.23<span class="sep">/</span><span class="cur">€</span>2.00</span></div>
    </div>
  </article>

  <article class="meal-card" style="top:479px">
    <div class="meal-photo photo-fries" role="img" aria-label="Photo of a bowl of french fries with ketchup"></div>
    <div class="meal-info">
      <h2 class="meal-name">Pommes frites</h2>
      <p class="meal-desc">text here to describe</p>
      <div class="rating"><svg class="star-on"><use href="#star"/></svg><svg class="star-on"><use href="#star"/></svg><svg class="star-on"><use href="#star"/></svg><svg class="star-off"><use href="#star"/></svg><svg class="star-off"><use href="#star"/></svg></div>
      <div class="price-tag"><span class="basket"><svg width="20" height="20"><use href="#basket"/></svg></span><span class="amounts"><span class="cur">€</span>0.70<span class="sep">/</span><span class="cur">€</span>1.00</span></div>
    </div>
  </article>

  <article class="meal-card" style="top:636px">
    <div class="meal-photo photo-add"><svg width="80" height="80"><use href="#add-photo"/></svg></div>
    <div class="meal-info">
      <h2 class="meal-name">Maccaronelli</h2>
      <p class="meal-desc">maccaronelli</p>
      <div class="rating"><svg class="star-on"><use href="#star"/></svg><svg class="star-on"><use href="#star"/></svg><svg class="star-on"><use href="#star"/></svg><svg class="star-on"><use href="#star"/></svg><svg class="star-on"><use href="#star"/></svg></div>
    </div>
  </article>

  <aside class="ad-banner">
    <div class="ad-badge"></div>
    <div class="ad-artwork" role="img" aria-label="Game advertisement artwork with a castle by the sea"></div>
    <div class="ad-button">Spielen</div>
    <div class="ad-info">i</div>
  </aside>
</main>
</body>
</html>
```